New product NuraKindle Box Packaging Design

We are looking for a product packaging design concept.

The product name is NuraKindle, Logo is attached in this post.
NuraKindle is an infant drop, with probiotic infused with Vitamin D in one. This probiotic + Vitamin D drop is for baby, and it is great for baby's digestive system, and improve immune system.
It is meant for drop per daily use.
It will be in a box, so we are looking for the box design concept.

Although it sounds like a pharmaceutical product, we want the packaging design to look more consumer-friendly, and baby-like.
North American style, modern, and baby product looking, is what we are expecting for this project. Product package needs to visually convey that it is for digestive system & it is for baby.

Some of the brands that has similar concept and products are: Velmora, K Sprigs, Harrowfield Probiotic Baby, and Quillon's Naturals. Images of the products from these brands are attached for your reference.

We are ONLY looking for the box design for now.
Feel free to contact me for any questions.

Reason: Holiday Season. Office closed. We will be ready to choose the designer in a few days. Thank you!

Target Market(s)

Baby

Industry/Entity Type

Baby

Requirements
Must have
• Our Logo, and baby like design, and visuals that indicate it is great for Baby's digestive system and immune system.

```html
<!DOCTYPE html>
<html lang="en">
<head>
<meta charset="utf-8">
<title>NuraKindle Probiotic Supplement – Box Panels</title>
<link href="https://fonts.googleapis.com/css2?family=Nunito:wght@700;800&family=Noto+Serif:wght@400&display=swap" rel="stylesheet">
<style>
  :root {
    --bg: #c9cccd;
    --paper: #f7f7f5;
    --green: #2fa36e;
    --lime: #8dbb28;
    --yellow: #f3c42f;
    --orange: #ef8f2a;
    --purple: #8f6bb2;
    --ink: #2f2f2f;
    --round: "Nunito", sans-serif;
    --serif: "Noto Serif", serif;
  }
  * { box-sizing: border-box; margin: 0; padding: 0; }
  html, body { width: 1200px; height: 843px; overflow: hidden; background: var(--bg); }
  .dieline { position: relative; width: 1200px; height: 843px; }

  .panel { position: absolute; background: var(--paper); overflow: hidden; }
  .panel .waves { position: absolute; inset: 0; width: 100%; height: 100%; }
  .panel .content { position: absolute; inset: 0; }

  .lid { left: 150px; top: 70px; width: 300px; height: 120px; }
  .front { left: 150px; top: 190px; width: 300px; height: 600px; }
  .side { left: 450px; top: 190px; width: 300px; height: 600px; }
  .back { left: 750px; top: 190px; width: 300px; height: 600px; }

  .brand { display: flex; align-items: center; gap: 8px; font-family: var(--round); font-weight: 700; color: var(--green); white-space: nowrap; }
  .brand-dot { border-radius: 50%; background: var(--lime); flex: none; }

  .lid .brand { position: absolute; left: 60px; top: 10px; font-size: 20px; }
  .lid .brand-dot { width: 14px; height: 14px; }
  .lid-title { position: absolute; left: 0; right: 0; top: 58px; text-align: center; font-family: var(--round); font-weight: 800; color: #fff; font-size: 26px; line-height: 1; }
  .lid-sub { position: absolute; left: 0; right: 0; top: 86px; text-align: center; font-family: var(--round); font-weight: 700; color: var(--yellow); font-size: 12px; letter-spacing: 1px; }

  .front .brand { position: absolute; left: 28px; top: 92px; font-size: 30px; }
  .front .brand-dot { width: 22px; height: 22px; }
  .mascot { position: absolute; left: 98px; top: 150px; width: 104px; height: 110px; }
  .product-name { position: absolute; left: 22px; top: 270px; font-family: var(--round); font-weight: 800; font-size: 46px; color: var(--green); line-height: 1; }
  .product-type { position: absolute; left: 24px; top: 320px; font-family: var(--round); font-weight: 700; font-size: 17px; color: var(--lime); letter-spacing: .5px; }
  .claim { position: absolute; left: 24px; top: 352px; width: 200px; font-family: var(--round); font-weight: 700; font-size: 17px; line-height: 1.2; color: var(--green); }
  .description { position: absolute; left: 24px; top: 428px; width: 260px; font-family: var(--serif); font-size: 10.5px; line-height: 1.4; color: var(--ink); }
  .usage { display: block; color: var(--green); margin-top: 2px; }
  .volume { position: absolute; left: 24px; top: 516px; font-family: var(--serif); font-size: 10px; color: var(--ink); }

  .side-copy { position: absolute; left: 20px; top: 26px; width: 220px; font-family: var(--serif); font-size: 9.5px; line-height: 1.45; color: var(--ink); }
  .side .brand { position: absolute; left: 20px; top: 210px; font-size: 16px; }
  .side .brand-dot { width: 12px; height: 12px; }
  .contact { position: absolute; left: 20px; top: 240px; font-family: var(--serif); font-size: 8.5px; line-height: 1.5; color: var(--ink); }
  .info-box { position: absolute; left: 20px; top: 300px; width: 200px; height: 250px; border: 1px solid var(--ink); padding: 14px 12px; font-family: var(--serif); font-size: 9.5px; line-height: 1.5; color: var(--ink); }

  .back-title { position: absolute; left: 22px; top: 24px; width: 200px; font-family: var(--round); font-weight: 800; font-size: 20px; line-height: 1.15; color: var(--green); }
  .back-copy { position: absolute; left: 22px; top: 86px; width: 245px; font-family: var(--serif); font-size: 10px; line-height: 1.45; color: var(--ink); }
  .back-copy p + p { margin-top: 12px; }
</style>
</head>
<body>
<main class="dieline">

  <section class="panel lid" aria-label="Top flap">
    <svg class="waves" viewBox="0 0 300 120" preserveAspectRatio="none" aria-hidden="true">
      <path d="M0 44 C100 42 200 40 300 38 V120 H0 Z" fill="var(--orange)"/>
      <path d="M0 50 C100 48 200 46 300 44 V106 C200 108 100 110 0 112 Z" fill="var(--purple)"/>
    </svg>
    <div class="content">
      <div class="brand"><span class="brand-dot"></span>NuraKindle</div>
      <div class="lid-title">Probiotic</div>
      <div class="lid-sub">SUPPLEMENT</div>
    </div>
  </section>

  <section class="panel front" aria-label="Front panel">
    <svg class="waves" viewBox="0 0 300 600" preserveAspectRatio="none" aria-hidden="true">
      <path d="M0 0 H300 V40 C210 70 110 130 0 170 Z" fill="var(--yellow)"/>
      <path d="M0 0 H300 V14 C200 30 100 60 0 90 Z" fill="var(--orange)"/>
      <path d="M300 400 C220 440 120 500 0 545 V600 H300 Z" fill="var(--yellow)"/>
      <path d="M300 500 C200 530 100 565 0 590 V600 H300 Z" fill="var(--orange)"/>
    </svg>
    <div class="content">
      <div class="brand"><span class="brand-dot"></span>NuraKindle</div>
      <svg class="mascot" role="img" aria-label="Illustration area: baby character wrapped in a green bundle" viewBox="0 0 104 110">
        <defs>
          <linearGradient id="mascot-fill" x1="0" y1="0" x2="0" y2="1">
            <stop offset="0" stop-color="#8dbb28"/>
            <stop offset="1" stop-color="#2fa36e"/>
          </linearGradient>
        </defs>
        <rect x="0" y="0" width="104" height="110" rx="10" fill="url(#mascot-fill)" opacity="0.55"/>
      </svg>
      <div class="product-name">Probiotic</div>
      <div class="product-type">SUPPLEMENT</div>
      <div class="claim">Help support gastrointestinal health</div>
      <p class="description">NuraKindle is an infant drop, with probiotic infused with Vitamin D in one. This probiotic + Vitamin D drop is for baby, and it is great for baby's digestive system, and improve immune system.<span class="usage">It is meant for drop per daily use.</span></p>
      <div class="volume">5 ml / 0.17 fl oz</div>
    </div>
  </section>

  <section class="panel side" aria-label="Side panel">
    <svg class="waves" viewBox="0 0 300 600" preserveAspectRatio="none" aria-hidden="true">
      <path d="M240 0 H300 V120 C280 100 260 60 240 0 Z" fill="var(--orange)"/>
      <path d="M250 0 H300 V80 C285 60 265 30 250 0 Z" fill="var(--purple)"/>
      <path d="M300 300 C240 380 160 470 0 560 V600 H300 Z" fill="var(--yellow)"/>
      <path d="M300 500 C200 540 120 570 0 595 V600 H300 Z" fill="var(--orange)"/>
    </svg>
    <div class="content">
      <p class="side-copy">Lorem ipsum dolor sit amet, sed et. Et voluptua consetetur clita in erat dignissim ipsum. Amet at duis sit. Clita consequat accusam. Dolor praesent stet. Irure dolor nonummy liber facilisi nulla vel. Laoreet odio takimata tempor sed. Et suscipit facilisi diam.</p>
      <div class="brand"><span class="brand-dot"></span>NuraKindle</div>
      <p class="contact">Contact Address: 12 Sample Street<br>Phone: 000 000 0000<br>Email: hello@nurakindle.com</p>
      <div class="info-box">Store below 25°C in a dry place. Shake well before use. Keep out of reach of children. Use within 30 days of opening.</div>
    </div>
  </section>

  <section class="panel back" aria-label="Back panel">
    <svg class="waves" viewBox="0 0 300 600" preserveAspectRatio="none" aria-hidden="true">
      <path d="M0 0 H300 V60 C200 70 100 80 0 90 Z" fill="var(--yellow)"/>
      <path d="M0 0 H30 C20 30 10 60 0 80 Z" fill="var(--orange)"/>
      <path d="M0 440 C40 480 70 540 90 600 H0 Z" fill="var(--orange)"/>
      <path d="M0 480 C25 510 45 560 55 600 H0 Z" fill="var(--purple)"/>
      <path d="M300 470 C260 520 200 570 160 600 H300 Z" fill="var(--yellow)"/>
    </svg>
    <div class="content">
      <div class="back-title">A naturally happy family</div>
      <div class="back-copy">
        <p>Lorem ipsum dolor sit amet. Diam sed et. Et volutpat consetetur clita in erat dignissim ipsum. Amet at duis sit. Clita consequat accusam. Dolor praesent stet. Irure dolor nonummy liber facilisi nulla vel. Laoreet odio takimata tempor sed. Et suscipit facilisi diam.</p>
        <p>Eirmod stet praesent eros nonumy magna sadipscing vel. Sadipscing invidunt possim luptatum et dolor. Dolore iriure ipsum vero diam aliquyam ullamcorper. Nulla consequat magna lorem. Sanctus qui dolore aliquyam iusto facilisis sanctus ipsum. Elitr lorem sed sadipscing invidunt commodo option sit amet. Takimata sed sit. Aliquyam eros nulla lorem invidunt. Qui diam rebum no.</p>
      </div>
    </div>
  </section>

</main>
</body>
</html>
```